Legal firm website redesign

Existing site for Sydney CBD lawyer needs clean and professional redesign - http://brennicklaw.com.au

The site will be viewed by a wide range of users: businesses, individuals, referral partners and other lawyers.

Please see the list of must haves for further details

Target Market(s)

Businesses, individuals, referral partners and other lawyers

Industry/Entity Type

Lawyer

Requirements
Must have
• Prominent display of phone number.
List of services down the left hand side of the site (5x services or so).
Search box in header.
Please use the greys and blues from the existing header.
New header must include the wording "Efficiency - Fulfillment - Integrity - Teamwork"

```html
<!DOCTYPE html>
<html lang="en">
<head>
<meta charset="utf-8">
<title>Brennick Law</title>
<link rel="stylesheet" href="https://fonts.googleapis.com/css2?family=Open+Sans:wght@400;600;700;800&display=swap">
<style>
  :root {
    --page-bg: #e3e3e3;
    --panel-bg: #e9e9e9;
    --panel-inner: #ececec;
    --ink: #222222;
    --white: #ffffff;
    --link-blue: #2f4fc4;
    --nav-dark-top: #7b7b7b;
    --nav-dark-bottom: #4e4e4e;
    --nav-light-top: #e6e6e6;
    --nav-light-bottom: #bdbdbd;
    --nav-active-text: #bcd8ff;
    --sky-top: #5b6e80;
    --sky-mid: #2d3d4d;
    --sky-bottom: #0f1a24;
    --hero-top: #58768f;
    --hero-bottom: #101c28;
    --footer-top: #9a9a9a;
    --footer-bottom: #b4b4b4;
    --rule: #c9c9c9;
  }
  * { margin: 0; padding: 0; box-sizing: border-box; }
  html, body { width: 1200px; height: 1126px; overflow: hidden; }
  body {
    position: relative;
    background: var(--page-bg);
    font-family: Arial, Helvetica, sans-serif;
    color: var(--ink);
  }
  .site-header {
    position: absolute; left: 0; top: 0; width: 1200px; height: 244px;
    background: linear-gradient(180deg, var(--sky-top) 0%, #7d8e9e 35%, var(--sky-mid) 62%, var(--sky-bottom) 100%);
  }
  .brand {
    position: absolute; left: 120px; top: 70px;
    font-family: "Open Sans", sans-serif; font-weight: 800;
    font-size: 52px; line-height: 56px; color: var(--white); letter-spacing: 1px;
  }
  .header-phone {
    position: absolute; left: 733px; top: 104px;
    font-family: "Open Sans", sans-serif; font-weight: 700;
    font-size: 22px; color: var(--white);
  }
  .footer-band {
    position: absolute; left: 0; top: 938px; width: 1200px; height: 188px;
    background: linear-gradient(180deg, var(--footer-top), var(--footer-bottom));
  }
  .main-panel {
    position: absolute; left: 367px; top: 220px; width: 770px; height: 760px;
    background: var(--panel-bg);
    box-shadow: 0 0 14px rgba(0,0,0,0.25);
  }
  .tab {
    position: absolute; width: 191px; height: 38px;
    background: linear-gradient(180deg, #8a8a8a, #555555);
    border-radius: 3px;
    box-shadow: 0 2px 4px rgba(0,0,0,0.35);
    font-family: "Open Sans", sans-serif; font-weight: 700; font-size: 14px;
    color: var(--white); text-align: center; line-height: 38px;
  }
  .tab-about { left: 881px; top: 196px; }
  .tab-recent { left: 880px; top: 712px; height: 42px; line-height: 42px; }
  .hero {
    position: absolute; left: 390px; top: 244px; width: 724px; height: 310px;
    background: radial-gradient(ellipse at 65% 60%, #b7c6d2 0%, var(--hero-top) 30%, var(--hero-bottom) 85%);
  }
  .values { position: absolute; left: 422px; top: 262px; list-style: none; }
  .values li {
    display: flex; align-items: center; height: 42px;
    font-family: "Open Sans", sans-serif; font-weight: 700; font-size: 29px; color: var(--white);
  }
  .values svg { width: 44px; height: 36px; margin-right: 6px; }
  .about-text {
    position: absolute; left: 379px; top: 566px; width: 746px; height: 120px;
    background: var(--panel-inner);
    padding: 4px 12px; font-size: 11.6px; line-height: 13.5px;
  }
  .about-text p { margin-bottom: 13px; }
  .indent { padding-left: 42px; }
  .recent-list { position: absolute; left: 380px; top: 760px; width: 724px; list-style: none; }
  .recent-list li {
    height: 14px; line-height: 13px; font-size: 11.4px; padding-left: 14px;
    border-bottom: 1px solid var(--rule);
  }
  .recent-list li.is-link { color: var(--link-blue); }
  .side-nav { position: absolute; left: 61px; top: 280px; width: 278px; list-style: none; }
  .side-nav li {
    height: 36px; margin-bottom: 1px; border-radius: 3px;
    font-family: "Open Sans", sans-serif; font-weight: 700;
    display: flex; align-items: center;
    box-shadow: 0 1px 3px rgba(0,0,0,0.3);
  }
  .nav-main { background: linear-gradient(180deg, var(--nav-dark-top), var(--nav-dark-bottom)); color: var(--white); font-size: 14px; padding-left: 48px; }
  .nav-main.is-active { color: var(--nav-active-text); }
  .nav-sub { background: linear-gradient(180deg, var(--nav-light-top), var(--nav-light-bottom)); color: var(--ink); font-size: 12.6px; padding-left: 22px; }
  .nav-gap { margin-top: 2px; }
  .search-box {
    position: absolute; left: 61px; top: 620px; width: 278px; height: 38px;
    background: linear-gradient(180deg, #f2f2f2, #c4c4c4);
    border-radius: 3px; box-shadow: 0 1px 3px rgba(0,0,0,0.3);
    font-size: 14px; color: #444; line-height: 38px; padding-left: 28px;
  }
  .search-box svg { position: absolute; right: 10px; top: 2px; width: 40px; height: 34px; }
  .footer-links {
    position: absolute; left: 367px; top: 1024px;
    font-size: 11.4px; color: var(--white);
  }
  .footer-contact {
    position: absolute; left: 934px; top: 1022px;
    font-size: 11.4px; line-height: 16px; color: var(--white);
  }
</style>
</head>
<body>
  <header class="site-header" role="img" aria-label="City skyline with a bridge over water at dusk"></header>
  <div class="brand">BRENNICK<br>LAW</div>
  <div class="header-phone">Call Us Today: (02) 9000 4821</div>

  <div class="footer-band"></div>

  <main class="main-panel"></main>
  <div class="tab tab-about">About us</div>

  <div class="hero" role="img" aria-label="Two business people shaking hands"></div>
  <ul class="values">
    <li><svg viewBox="0 0 44 36"><path d="M4 18 L16 30 L40 4" fill="none" stroke="#fff" stroke-width="4" stroke-linecap="round"/></svg>Efficiency</li>
    <li><svg viewBox="0 0 44 36"><path d="M4 18 L16 30 L40 4" fill="none" stroke="#fff" stroke-width="4" stroke-linecap="round"/></svg>Fulfillment</li>
    <li><svg viewBox="0 0 44 36"><path d="M4 18 L16 30 L40 4" fill="none" stroke="#fff" stroke-width="4" stroke-linecap="round"/></svg>&nbsp;Integrity</li>
    <li><svg viewBox="0 0 44 36"><path d="M4 18 L16 30 L40 4" fill="none" stroke="#fff" stroke-width="4" stroke-linecap="round"/></svg>Teamwork</li>
  </ul>

  <section class="about-text">
    <p><span class="indent"></span>Brennick Law is a dynamic commercial law firm in the CBD of Sydney providing services to corporate, small business and private clients. Brennick Law brings together over 30 years of experience in legal practice.<br>The strong focus of the firm is on commercial law and estate planning.</p>
    <p><span class="indent"></span>Brennick Law is committed to providing quality legal services in helping its clients achieve their objectives by providing a proactive understanding of its clients' businesses and creative legal solutions.</p>
  </section>

  <div class="tab tab-recent">Recent Additions</div>
  <ul class="recent-list">
    <li>Commencement of the Succession Act 2006 25.03.08</li>
    <li>Is that will valid? 15.01.08</li>
    <li class="is-link">Labor's proposed changes to IR laws 14.12.07</li>
    <li>Should you make your own will? 14.11.07</li>
    <li>Illegal workers 14.08.07</li>
    <li>Employees' liability for misleading or deceptive conduct 14.08.07</li>
    <li>Correct use of ACNs and ABNs 14.08.07</li>
    <li>Power of Attorney Infosheet 10.08.07</li>
    <li>Intestate Estates Infosheet 08.08.07</li>
    <li>Estate Planning Infosheet 07.06.07</li>
    <li>Special Disability Trusts Infosheet 18.05.07</li>
    <li>Testamentary Trusts Infosheet 17.05.07</li>
    <li>Appointment of an Enduring Guardian Infosheet 15.05.07</li>
  </ul>

  <ul class="side-nav">
    <li class="nav-main">Home</li>
    <li class="nav-main">About Us</li>
    <li class="nav-main is-active">Areas of Law</li>
    <li class="nav-sub">Commercial/Business Transactions</li>
    <li class="nav-sub">Commercial Litigation</li>
    <li class="nav-sub">Estate Planning &amp; Succession</li>
    <li class="nav-main nav-gap">Publications</li>
    <li class="nav-main">Contacts</li>
  </ul>

  <div class="search-box">Search...
    <svg viewBox="0 0 40 34"><circle cx="24" cy="13" r="9" fill="none" stroke="#111" stroke-width="3"/><path d="M17 20 L6 31" stroke="#111" stroke-width="5" stroke-linecap="round"/></svg>
  </div>

  <nav class="footer-links">Home | About Us | Area of Law | Our People | Publications | Contact</nav>
  <address class="footer-contact" style="font-style:normal">
    Telephone (02) 9000 4821<br>
    Facsimile (02) 9000 4822<br>
    Email info@brennicklaw.com.au
  </address>
</body>
</html>
```